Harlowe Wine Label - Design a front and smaller back label for an exclusive red wine

Harlowe Wines produces a very high quality, high priced wine from an old and prestigous vineyard in one of Australia's oldest, but smallest wine growing regions. The grapevines are old (like old men with gnarled arms and trunks) and they produce fewer grapes than younger vines but the grape quality (and thus wine quality) is magnificent and highly sought after as it produces wine of exceptional quality.
The vineyard was purchased by the Harlowe family in February 2010 from a multinational wine company who made wonderful, trophy winning wines for 10 years before the vineyard went into a decline.
The challenge is to produce 2 labels - a simple main front label that focuses on the Harlowe brand and a smaller, information rich, back label that relates the history of the vineyard.
The labels should have a white or charcoal grey background and impart tradition, quality, exclusivity and a little self indulgence which is why we want the family crest incorporated - the choice of font will help.
It might also impart a sense of fun so that it appeals to the 25-35 year old age bracket.
The label should be kept clean and simple not loud and busy. Preferred colours are black, grey and white. Red is fine if used sparingly

Here are the details:_

Front Label (115 long x 65-90mm wide)

Harlowe
Lanternfield Reserve
2011
Mudgee
Wine of Australia 750ml

Back Label (dimensions to suit text and front label design; font size small; text in black so that it is readable in less than optimal light (eg candlelight at a restaurant table).

Harlowe
Lanternfield Reserve 2011

This is the first release of The Lanternfield’s Reserve – just 100 dozen bottles were made. The wine was made from Shiraz and 10% Cabernet Sauvignon grapes sourced from an iconic Mudgee vineyard that was established 1966 by Peter Kell. In 1994, the vineyard known as ”Silverbrook”, became the source of a decade of formidable, trophy winning wines under Ashgrove’s and later Penwick’s ownership. The 20ha vineyard was purchased by Morag & Helen Harlowe in 2010. The Silverbrook name was retained by Penwicks; no wine has been released under this label since the 2006 vintage.

The shaky old Shiraz vines are slowly being restored to full health using careful cane pruning techniques that stimulates fresh, new tissue growth, more even bunch sizes and better grape quality and consistency. The Shiraz grapes used in this wine were hand-picked from two rows of the first crop from the 46 year old, cane pruned vines. The 2011 Reserve is the first step to re-establish the traditions of a famous vineyard and one of Australia’s most sought after export wines.

“Deep and intense purple hues with aromas of ripe blackberry fruits, spice and eucalypt with rich chocolate complemented by subtle oak overtones. A rich and full bodied wine exhibiting a soft yet generous palate with plum, forest fruits and mint chocolate notes. A fine grained tannin structure displaying integrated oak characters adds to the complexity of the wine. This wine was aged for 18 months in a blend of new French oak hogsheads and one year old American hogsheads, crafting a blend with great structure and length of flavour which will develop into a Mudgee classic” – Owen Pratley, Winemaker

13.5% Alc/Vol.
Contains approx 8.0 std drinks
Preservative (220) added

Harlowe Wines
Tallowby Rd, Mudgee 2850
www.harlowewines-example.com.au

Reason: My apologies to the designers who have kindly submitted some wonderful designs. I am trying to achieve a conscentious between shareholders. This is difficult as they are in different parts of the world and I have learned through this experience that opinions on wine labels are quite diverse!!! The feedback I have received so far indicates the following (1) A light or white background is preferred (2) The crest should not be a dominant part of the label (3) The label needs to be clean, fresh and uncomplicated (4) If red is used it should be in minor detail only (5) "Harlowe" should be distinctive. The font is difficult for us! (6) We are considering "The Lanternfield" RESERVE instead of "Lanternfield" RESERVE (7) The text on the back label is too long; I will edit and re-upload Many thanks for your help and patience Kind regards Morag

Good Morning All,
I have edited the back label text to reduce the size of the label. A Word file with the changes has just been uploaded.
Cheers
Morag

Dear Designers,
Thank you all so very much for the wonderful selection of designs you have submitted my family have all been overwhelmed by the quality and skill level exhibited and we all appreciate you your efforts
Kindest regards
Morag

Target Market(s)

25-35 year old men and women of Australia, China, US & UK

Industry/Entity Type

Restaurant

Requirements
Must have
• Crest
Should not have
• Animals on the label

```html
<!DOCTYPE html>
<html lang="en">
<head>
<meta charset="utf-8">
<title>Harlowe Wines – The Lanternfield Reserve labels</title>
<link rel="stylesheet" href="https://fonts.googleapis.com/css2?family=Bodoni+Moda:wght@400;500&family=Libre+Baskerville&display=swap">
<style>
  :root {
    --page: #ffffff;
    --band: #3b3c3e;
    --band-text: #b9babc;
    --ink: #1f1f1f;
    --ink-soft: #555555;
    --ink-muted: #7a7a7a;
    --crest: #f1f1f2;
    --crest-edge: #e4e4e6;
    --shadow: rgba(0,0,0,0.28);
  }
  * { margin: 0; padding: 0; box-sizing: border-box; }
  html, body { width: 1197px; height: 1200px; overflow: hidden; background: var(--page); }
  body { position: relative; font-family: "Libre Baskerville", "Times New Roman", serif; color: var(--ink); }

  .label {
    position: absolute;
    top: 277px;
    width: 500px;
    height: 645px;
    background: var(--page);
    box-shadow: 2px 3px 8px var(--shadow);
    overflow: hidden;
  }
  .label--front { left: 60px; }
  .label--back  { left: 637px; }

  .label__band {
    position: absolute; left: 0; top: 0; bottom: 0; width: 78px;
    background: var(--band);
  }
  .label__vintage {
    position: absolute; top: 24px; left: 0; width: 78px;
    text-align: center; color: var(--band-text);
    font-family: "Bodoni Moda", serif; font-size: 22px; line-height: 30px; letter-spacing: 4px;
  }
  .label__origin {
    position: absolute; left: 39px; bottom: 28px;
    transform-origin: left center; transform: rotate(-90deg) translateY(8px);
    white-space: nowrap; color: var(--band-text);
    font-family: "Bodoni Moda", serif; font-size: 14px; letter-spacing: 6px;
  }

  .label__crest { position: absolute; left: 150px; width: 280px; }
  .label--front .label__crest { top: 70px; height: 530px; }
  .label--back  .label__crest { top: 60px; height: 530px; }

  .label__content {
    position: absolute; left: 78px; right: 0; top: 0; bottom: 0; text-align: center;
  }
  .brand {
    font-family: "Bodoni Moda", serif; font-weight: 400;
    color: var(--ink-muted); letter-spacing: 3px;
  }
  .title {
    font-family: "Bodoni Moda", serif; font-weight: 400;
    color: var(--ink-soft); letter-spacing: 2px; white-space: nowrap;
  }
  .tier {
    font-family: "Bodoni Moda", serif; color: var(--ink-muted); letter-spacing: 3px;
  }

  .label--front .brand { margin-top: 252px; font-size: 21px; }
  .label--front .title { margin-top: 8px; font-size: 43px; line-height: 50px; }
  .label--front .tier  { margin-top: 10px; font-size: 14px; }

  .label--back .brand { margin-top: 36px; font-size: 17px; }
  .label--back .title { margin-top: 2px; font-size: 28px; line-height: 36px; }
  .label--back .tier  { margin-top: 8px; font-size: 12px; }

  .story {
    margin: 32px auto 0; width: 360px;
    font-family: "Libre Baskerville", serif; font-size: 11.2px; line-height: 17px; color: var(--ink);
  }
  .story p + p { margin-top: 17px; }
  .details {
    margin-top: 22px;
    font-size: 10px; line-height: 17px; color: var(--ink);
  }

  .label__foot {
    position: absolute; left: 100px; right: 22px; bottom: 26px;
    display: flex; justify-content: space-between;
    font-family: "Libre Baskerville", serif; font-size: 15px; color: var(--ink-muted);
  }
  .label--back .label__foot { font-size: 13px; bottom: 22px; }
</style>
</head>
<body>

  <section class="label label--front">
    <div class="label__band">
      <div class="label__vintage">20<br>11</div>
      <div class="label__origin">Wine of Australia</div>
    </div>
    <svg class="label__crest" viewBox="0 0 280 530" role="img" aria-label="Faint family crest with motto ribbon and shield">
      <path d="M20 20 Q140 -10 260 20 L250 90 Q140 60 30 90 Z" fill="var(--crest)"/>
      <path d="M30 220 L250 220 L250 390 Q250 480 140 525 Q30 480 30 390 Z" fill="var(--crest)" stroke="var(--crest-edge)"/>
    </svg>
    <div class="label__content">
      <div class="brand">HARLOWE</div>
      <div class="title">The Lanternfield</div>
      <div class="tier">RESERVE</div>
    </div>
    <div class="label__foot"><span>750ml</span><span>13.5% Vol.</span></div>
  </section>

  <section class="label label--back">
    <div class="label__band">
      <div class="label__vintage">20<br>11</div>
      <div class="label__origin">Wine of Australia</div>
    </div>
    <svg class="label__crest" viewBox="0 0 280 530" role="img" aria-label="Faint family crest with motto ribbon and shield">
      <path d="M20 20 Q140 -10 260 20 L250 90 Q140 60 30 90 Z" fill="var(--crest)"/>
      <path d="M30 220 L250 220 L250 390 Q250 480 140 525 Q30 480 30 390 Z" fill="var(--crest)" stroke="var(--crest-edge)"/>
    </svg>
    <div class="label__content">
      <div class="brand">HARLOWE</div>
      <div class="title">The Lanternfield</div>
      <div class="tier">RESERVE</div>
      <div class="story">
        <p>The Shiraz and Cabernet grapes from which this wine was made were handpicked from a 20ha vineyard that was established in 1966. The vineyard formerly known as “Silverbrook” was purchased by the Harlowe family in 2010.</p>
        <p>The shaky old Shiraz vines are slowly being restored to full health using careful cane pruning techniques to achieve better grape quality and consistency. The 2011 Reserve is the first step to re-establish the traditions of a famous vineyard and one of Australia’s most sought after export wines.</p>
        <p>“Deep and intense purple hues with aromas of ripe blackberry fruits, spice and eucalypt with rich chocolate complemented by subtle oak overtones. A rich and full bodied wine exhibiting a soft yet generous palate with plum, forest fruits and mint chocolate notes. A fine grained tannin structure displaying integrated oak characters adds to the complexity of the wine. This wine was aged for 18 months in a blend of new French oak hogsheads and one year old American hogsheads, crafting a blend with great structure and length of flavour which will develop into a Mudgee classic” – Owen Pratley, Winemaker.</p>
        <div class="details">
          Contains approx 8.0 std drinks, Preservative (220) added<br>
          Tallowby Rd, Mudgee 2850<br>
          www.harlowewines-example.com.au
        </div>
      </div>
    </div>
    <div class="label__foot"><span>13.5 Vol.</span><span>750ml</span></div>
  </section>

</body>
</html>
```